Summer Fun

I need a Poster for Front of hotel advertising discounted drinks on Thursday & Fridays
$3.50.
Schooners of Local Beer, Glass of House Wine & Bubbly.
From 3.30pm to 6.30 pm
Nibblies Provided

25 + Market

Hotel

• Do not want to be known as Happy Hour.

```html
<!DOCTYPE html>
<html lang="en">
<head>
<meta charset="utf-8">
<title>Summer Fun – Thursday &amp; Friday Drinks Poster</title>
<link href="https://fonts.googleapis.com/css2?family=Arimo:wght@700&family=Didact+Gothic&family=Questrial&display=swap" rel="stylesheet">
<style>
  :root {
    --deep-red: #6e0c0c;
    --hot-red: #d91d10;
    --orange: #f38a12;
    --glow: #ffffff;
    --mist: #eef0f3;
    --mist-dark: #dfe2e7;
    --slate: #5d717c;
    --ink: #2b2b2b;
    --dots: #8a96a0;
  }
  html, body {
    margin: 0;
    padding: 0;
    overflow: hidden;
  }
  body {
    width: 856px;
    height: 1200px;
  }
  .poster {
    position: relative;
    width: 856px;
    height: 1200px;
    overflow: hidden;
    background: linear-gradient(180deg, var(--mist) 0%, #f7f8fa 60%, var(--mist-dark) 100%);
  }
  .tropical-scene {
    position: absolute;
    left: 0;
    top: 0;
    width: 856px;
    height: 820px;
    background:
      radial-gradient(ellipse 260px 220px at 400px 130px, var(--glow) 0%, rgba(255,255,255,0.85) 40%, rgba(255,255,255,0) 100%),
      radial-gradient(ellipse 200px 120px at 690px 140px, rgba(255,235,235,0.7) 0%, rgba(255,255,255,0) 100%),
      radial-gradient(ellipse 180px 110px at 110px 90px, rgba(255,225,225,0.6) 0%, rgba(255,255,255,0) 100%),
      linear-gradient(180deg, var(--deep-red) 0%, var(--hot-red) 30%, #a41410 52%, #c8383a 64%, rgba(240,240,243,0.6) 82%, rgba(247,248,250,0) 100%);
  }
  .time-band {
    position: absolute;
    left: 0;
    top: 0;
  }
  .time-band text {
    font-family: "Questrial", sans-serif;
    font-size: 20px;
    letter-spacing: 1px;
    fill: var(--ink);
  }
  .headline {
    position: absolute;
    left: 0;
    width: 856px;
    top: 282px;
    margin: 0;
    text-align: center;
    font-family: "Questrial", sans-serif;
    font-weight: 400;
    font-size: 108px;
    line-height: 96px;
    letter-spacing: -1px;
  }
  .headline span {
    display: block;
  }
  .headline .word-summer {
    padding-left: 8px;
    background: linear-gradient(90deg, #5a0a0a 0%, #b0160f 35%, var(--orange) 60%, #b0160f 80%, #3e0707 100%);
    -webkit-background-clip: text;
    background-clip: text;
    color: transparent;
  }
  .headline .word-fun {
    color: var(--orange);
  }
  .days {
    position: absolute;
    left: 0;
    width: 888px;
    top: 762px;
    margin: 0;
    text-align: center;
    font-family: "Arimo", sans-serif;
    font-weight: 700;
    font-size: 58px;
    letter-spacing: -1px;
    color: var(--slate);
  }
  .rule {
    position: absolute;
    height: 0;
    border-top: 2px dotted var(--dots);
  }
  .rule-top { left: 198px; width: 494px; top: 828px; }
  .rule-bottom { left: 162px; width: 534px; top: 1022px; }
  .offer {
    position: absolute;
    left: 0;
    width: 888px;
    top: 850px;
    margin: 0;
    text-align: center;
    font-family: "Didact Gothic", sans-serif;
    color: var(--ink);
  }
  .offer .item {
    display: block;
    font-size: 30px;
    line-height: 44px;
    letter-spacing: 1.5px;
  }
  .offer .price {
    display: block;
    font-size: 27px;
    line-height: 38px;
    margin-top: 2px;
  }
  .offer .extra {
    display: block;
    font-size: 13px;
    line-height: 14px;
    letter-spacing: 0.5px;
  }
  .tagline {
    position: absolute;
    left: 0;
    width: 888px;
    top: 1046px;
    margin: 0;
    text-align: center;
    font-family: "Arimo", sans-serif;
    font-weight: 700;
    font-size: 31px;
    letter-spacing: -0.5px;
    color: var(--slate);
  }
</style>
</head>
<body>
  <main class="poster">
    <div class="tropical-scene" role="img" aria-label="Red tropical sky with glowing light, clouds, sparkles and silhouetted palm trees fading into white mist"></div>

    <svg class="time-band" width="360" height="280" viewBox="0 0 360 280" aria-label="From 3.30 pm to 6.30 pm">
      <polygon points="0,212 272,0 340,0 0,266" fill="#f3f4f6" opacity="0.95"/>
      <text x="0" y="0" text-anchor="middle" transform="translate(186,100) rotate(-38)">FROM 3.30 PM TO 6.30 PM</text>
    </svg>

    <h1 class="headline">
      <span class="word-summer">SUMMER</span>
      <span class="word-fun">FUN</span>
    </h1>

    <h2 class="days">Thursdays &amp; Fridays</h2>
    <div class="rule rule-top"></div>

    <p class="offer">
      <span class="item">SCHOONERS OF LOCAL BEER</span>
      <span class="item">GLASS OF HOUSE WINE &amp; BUBBLY</span>
      <span class="price">$3.50</span>
      <span class="extra">NIBBLIES PROVIDED</span>
    </p>

    <div class="rule rule-bottom"></div>
    <p class="tagline">SHOW YOUR SUMMER SIDE</p>
  </main>
</body>
</html>
```